Canadian company needs a packaging design for a new product line of TubNova Hot Tub & Bath Fragran

We are looking for a packaging design for a new company based in Edmonton, Alberta Canada called TubNova. We are developing a new product line of liquid and crystal Hot Tub & Bath Fragrances (aromatherapy) for example Lavender will be one of our fragrances. We are looking at the possibilities of using a stand up pouch and or the standard plastic bottles for our fragrance line. There will be different sizes from 150 grams to 600 grams in the crystal and 275 ml in the liquid. We would like to see bright multi-colored designs possibly with picture of the fragrance or a theme like favorite drinks or a more sensual idea. Each one of our fragrances will be a different color the main design needs to be able to have a different color of liquid or crystal in the bottle and possibly parts of the label will change colors for each fragrance. I have attached samples of another brand that we want to improve on.

Target Market(s)

Most of these fragrance are bought by women 70% men 30%
age 25 - 55

Industry/Entity Type

It Company

Requirements
Must have
• bottle size
Fragrance name
Nice to have
• Using the files below I like the circle of colors and possibly it could be made using water drops like in the file and possibly the two "S" could be designed like the third file I just added

```html
<!DOCTYPE html>
<html lang="en">
<head>
<meta charset="utf-8">
<title>TubNova Lavender Packaging Label</title>
<link href="https://fonts.googleapis.com/css2?family=Questrial&display=swap" rel="stylesheet">
<style>
  :root {
    --purple: #8e2b8f;
    --purple-deep: #6c1f72;
    --purple-light: #a64aa6;
    --white: #ffffff;
    --silver: #dcdcdc;
    --green: #1e9a3e;
    --green-light: #3cc45c;
    --green-dark: #12702b;
    --gold: #9a7a22;
    --ink-purple: #5c1e63;
  }
  html, body {
    margin: 0;
    padding: 0;
    overflow: hidden;
    background: var(--white);
  }
  .label {
    position: relative;
    width: 1200px;
    height: 709px;
    overflow: hidden;
    font-family: "Questrial", "Century Gothic", sans-serif;
  }
  .label-art {
    position: absolute;
    inset: 0;
    display: block;
  }
  .brand-name {
    position: absolute;
    left: 0;
    width: 1160px;
    top: 62px;
    text-align: center;
    font-size: 78px;
    color: var(--purple);
    letter-spacing: 1px;
    margin: 0;
    font-weight: 400;
  }
  .ribbon-text {
    position: absolute;
    color: var(--white);
    white-space: nowrap;
    transform-origin: center;
  }
  .ribbon-text--spa {
    left: 120px;
    top: 536px;
    width: 220px;
    text-align: center;
    font-size: 30px;
    transform: rotate(-15deg);
  }
  .ribbon-text--aroma {
    left: 170px;
    top: 592px;
    width: 220px;
    text-align: center;
    font-size: 27px;
    transform: rotate(-15deg);
  }
  .fragrance-name {
    position: absolute;
    left: 830px;
    top: 596px;
    width: 180px;
    text-align: center;
    font-size: 36px;
    color: var(--white);
  }
  .net-weight {
    position: absolute;
    left: 500px;
    top: 636px;
    width: 190px;
    text-align: center;
    font-size: 20px;
    color: var(--gold);
  }
  .tagline {
    position: absolute;
    left: 0;
    width: 1200px;
    top: 676px;
    text-align: center;
    font-size: 21px;
    color: var(--ink-purple);
    margin: 0;
  }
</style>
</head>
<body>
<div class="label">
  <svg class="label-art" width="1200" height="709" viewBox="0 0 1200 709" aria-hidden="true">
    <defs>
      <linearGradient id="panel-gradient" x1="0" y1="0" x2="0" y2="1">
        <stop offset="0" stop-color="#8a2a8c"/>
        <stop offset="0.45" stop-color="#9a3a9b"/>
        <stop offset="1" stop-color="#8e2b8f"/>
      </linearGradient>
      <linearGradient id="wave-gradient" x1="0" y1="0" x2="0" y2="1">
        <stop offset="0" stop-color="#ffffff"/>
        <stop offset="0.6" stop-color="#f4f4f4"/>
        <stop offset="1" stop-color="#d8d8d8"/>
      </linearGradient>
      <radialGradient id="photo-gradient" cx="0.5" cy="0.6" r="0.6">
        <stop offset="0" stop-color="#b486d6"/>
        <stop offset="0.35" stop-color="#e9dcef"/>
        <stop offset="0.7" stop-color="#f2eef3"/>
        <stop offset="1" stop-color="#cfc3d6"/>
      </radialGradient>
      <linearGradient id="ribbon-gradient" x1="0" y1="0" x2="0" y2="1">
        <stop offset="0" stop-color="var(--green-light)"/>
        <stop offset="1" stop-color="var(--green)"/>
      </linearGradient>
      <linearGradient id="base-gradient" x1="0" y1="0" x2="0" y2="1">
        <stop offset="0" stop-color="#ffffff"/>
        <stop offset="1" stop-color="#e6e6e6"/>
      </linearGradient>
      <clipPath id="photo-clip">
        <circle cx="600" cy="650" r="335"/>
      </clipPath>
    </defs>

    <rect class="panel" x="0" y="0" width="1200" height="709" fill="url(#panel-gradient)"/>

    <path class="top-wave" d="M0,0 H965 C900,20 840,235 590,235 C340,235 220,28 0,26 Z" fill="url(#wave-gradient)"/>

    <circle class="photo-ring" cx="600" cy="650" r="362" fill="var(--purple-deep)"/>
    <rect class="product-photo" role="img" aria-label="Photo of purple lavender bath crystals in a white bowl with lavender sprigs and oil bottles"
          x="200" y="300" width="800" height="400" clip-path="url(#photo-clip)" fill="url(#photo-gradient)"/>

    <circle class="fragrance-badge" cx="930" cy="660" r="120" fill="var(--purple-deep)"/>

    <path class="weight-tab" d="M488,662 L500,636 Q504,630 512,630 H688 Q696,630 700,636 L712,662 Z" fill="var(--white)"/>

    <g class="ribbon ribbon--spa" transform="rotate(-15 230 560)">
      <polygon points="95,548 125,548 125,590 95,590 108,569" fill="var(--green-dark)"/>
      <rect x="115" y="534" width="230" height="50" fill="url(#ribbon-gradient)"/>
    </g>
    <g class="ribbon ribbon--aroma" transform="rotate(-15 280 610)">
      <rect x="170" y="588" width="220" height="44" fill="url(#ribbon-gradient)"/>
      <polygon points="390,600 415,600 402,618 415,638 390,638" fill="var(--green-dark)"/>
    </g>

    <rect class="base-band" x="0" y="662" width="1200" height="47" fill="url(#base-gradient)"/>
  </svg>

  <h1 class="brand-name">TubNova</h1>
  <div class="ribbon-text ribbon-text--spa">Spa &amp; Bath</div>
  <div class="ribbon-text ribbon-text--aroma">Aromatherapy</div>
  <div class="fragrance-name">Lavander</div>
  <div class="net-weight">100g Net</div>
  <p class="tagline">A great aroma start to a well balanced body</p>
</div>
</body>
</html>
```